Fontenot Bayou Grillhouse (Owners Card)

Need a classy, but modern business card. I have included a promotional card for the steakhouse. I need one for myself (the owner) that is more professional.

Target Market(s)

General Public

Industry/Entity Type

Food service

Contact Information for Business Card

Name, business address, phone number, email, logo

Font styles to use
Serif
Sans Serif
Decorative
Script

Requirements
Must have
• My name (Darvel Pruitt), business address (327 Oakmere Street), phone number (510) 493-2615, email (Dpruittkr4@mailvane.example. On the back of the card: Psalms 27 1 The LORD is my light and my salvation— whom shall I fear? The LORD is the stronghold of my life— of whom shall I be afraid? 2 When the wicked advance against me to devour me, it is my enemies and my foes who will stumble and fall. 3 Though an army besiege me, my heart will not fear; though war break out against me, even then I will be confident.
Nice to have
• Something that’s bold, but modern and professional.

```html
<!DOCTYPE html>
<html lang="en">
<head>
<meta charset="utf-8">
<title>Fontenot Bayou Grillhouse – Owner's Card</title>
<link rel="stylesheet" href="https://fonts.googleapis.com/css2?family=Lato:ital,wght@0,400;0,700;0,900;1,400&family=Great+Vibes&display=swap">
<style>
  :root {
    --bg: #2a2a2a;
    --card: #1c1c1c;
    --text: #e8e8e8;
    --muted: #cfcfcf;
    --green: #1ee61a;
    --yellow: #e8d400;
    --orange: #ff8a00;
    --red: #ff1a0a;
    --ink: #111111;
  }
  * { box-sizing: border-box; margin: 0; padding: 0; }
  html, body { width: 1200px; height: 875px; overflow: hidden; }
  body {
    background: var(--bg);
    font-family: "Lato", Arial, sans-serif;
    position: relative;
  }
  .card {
    position: absolute;
    width: 640px;
    height: 366px;
    background: var(--card);
    box-shadow: 0 18px 40px rgba(0,0,0,.55);
    overflow: hidden;
  }

  /* Back card */
  .card--back { left: 50px; top: 40px; }
  .back__frame { position: absolute; left: 36px; top: 36px; width: 568px; height: 294px; }
  .back__brand {
    position: absolute; left: 50%; top: 22px; transform: translateX(-50%);
    background: var(--card); padding: 0 12px;
    display: flex; align-items: center; gap: 8px;
    font-weight: 700; font-size: 15px; color: var(--orange); white-space: nowrap;
  }
  .back__brand-dot { width: 12px; height: 12px; border-radius: 50%; background: var(--orange); }
  .verse {
    position: absolute; left: 60px; right: 60px; top: 86px;
    text-align: center; color: var(--text); font-size: 14.5px; line-height: 1.45;
  }
  .verse p + p { margin-top: 16px; }
  .back__ref {
    position: absolute; left: 50%; bottom: 18px; transform: translateX(-50%);
    background: var(--card); padding: 0 14px;
    font-family: "Great Vibes", cursive; font-size: 32px; line-height: 1;
    background-image: linear-gradient(90deg, var(--red), var(--orange), var(--green));
    -webkit-background-clip: text; background-clip: text; color: transparent;
  }
  .back__ref-mask { position: absolute; left: 50%; bottom: 30px; transform: translateX(-50%); width: 160px; height: 12px; background: var(--card); }

  /* Front card */
  .card--front { left: 510px; top: 468px; }
  .front__brand {
    position: absolute; left: 40px; top: 130px; width: 290px;
    display: flex; align-items: center; gap: 12px;
    font-weight: 900; font-size: 27px; line-height: 1.1; color: var(--green);
  }
  .front__brand-dot { flex: none; width: 22px; height: 22px; border-radius: 50%; background: var(--orange); }
  .owner { position: absolute; left: 352px; top: 34px; }
  .owner__name { font-weight: 700; font-size: 32px; color: var(--green); line-height: 1; }
  .owner__role {
    font-family: "Great Vibes", cursive; font-size: 28px; line-height: 1.1; margin-left: 4px;
    background-image: linear-gradient(90deg, var(--orange), var(--red));
    -webkit-background-clip: text; background-clip: text; color: transparent;
  }
  .contact { position: absolute; left: 356px; top: 122px; list-style: none; color: var(--muted); font-size: 14px; line-height: 1.4; }
  .contact li { display: flex; gap: 9px; align-items: flex-start; }
  .contact li + li { margin-top: 3px; }
  .contact svg { flex: none; width: 13px; height: 13px; margin-top: 3px; fill: var(--green); }
  .tagline {
    position: absolute; left: 0; right: 0; bottom: 0; height: 60px;
    background: linear-gradient(90deg, var(--red) 0%, var(--orange) 35%, var(--yellow) 65%, var(--green) 100%);
    display: flex; align-items: center; justify-content: center;
    color: var(--ink); font-size: 22px; white-space: nowrap;
  }
  .tagline strong { font-weight: 900; margin: 0 6px; }
</style>
</head>
<body>

<section class="card card--back" aria-label="Card back">
  <svg class="back__frame" viewBox="0 0 568 294" preserveAspectRatio="none" aria-hidden="true">
    <defs>
      <linearGradient id="frameGrad" x1="0" y1="1" x2="1" y2="0">
        <stop offset="0" stop-color="#1ee61a"/>
        <stop offset=".45" stop-color="#e8d400"/>
        <stop offset=".7" stop-color="#ff8a00"/>
        <stop offset="1" stop-color="#ff1a0a"/>
      </linearGradient>
    </defs>
    <rect x="1" y="1" width="566" height="292" fill="none" stroke="url(#frameGrad)" stroke-width="2"/>
  </svg>
  <div class="back__brand"><span class="back__brand-dot"></span>Fontenot Bayou</div>
  <div class="verse">
    <p>The LORD is my light and my salvation— whom shall I fear?<br>The LORD is the stronghold of my life— of whom shall I be afraid?</p>
    <p>When the wicked advance against me to devour me,<br>it is my enemies and my foes who will stumble and fall.</p>
    <p>Though an army besiege me, my heart will not fear;<br>though war break out against me, even then I will be confident.</p>
  </div>
  <div class="back__ref-mask"></div>
  <div class="back__ref">Psalms 27 1</div>
</section>

<section class="card card--front" aria-label="Card front">
  <div class="front__brand"><span class="front__brand-dot"></span>Fontenot Bayou Grillhouse</div>
  <div class="owner">
    <div class="owner__name">Darvel Pruitt</div>
    <div class="owner__role">Owner</div>
  </div>
  <ul class="contact">
    <li>
      <svg viewBox="0 0 24 24" aria-hidden="true"><path d="M12 2a7 7 0 0 0-7 7c0 5 7 13 7 13s7-8 7-13a7 7 0 0 0-7-7zm0 9.5A2.5 2.5 0 1 1 12 6.5a2.5 2.5 0 0 1 0 5z"/></svg>
      <span>327 Oakmere Street<br>Millbrook, CA 94590</span>
    </li>
    <li>
      <svg viewBox="0 0 24 24" aria-hidden="true"><path d="M6.6 10.8a15.1 15.1 0 0 0 6.6 6.6l2.2-2.2a1 1 0 0 1 1-.25 11.4 11.4 0 0 0 3.6.57 1 1 0 0 1 1 1V20a1 1 0 0 1-1 1A17 17 0 0 1 3 4a1 1 0 0 1 1-1h3.5a1 1 0 0 1 1 1c0 1.25.2 2.45.57 3.6a1 1 0 0 1-.25 1z"/></svg>
      <span>(510) 493-2615</span>
    </li>
    <li>
      <svg viewBox="0 0 24 24" aria-hidden="true"><path d="M3 5h18v14H3zm2 2v.5l7 4.5 7-4.5V7z"/></svg>
      <span>Dpruittkr4@mailvane.example</span>
    </li>
    <li>
      <svg viewBox="0 0 24 24" aria-hidden="true"><path d="M12 2a10 10 0 1 0 0 20 10 10 0 0 0 0-20zm6.9 9h-3a15 15 0 0 0-1.4-6A8 8 0 0 1 18.9 11zM12 4c.9 1.3 1.7 3.9 1.9 7h-3.8C10.3 7.9 11.1 5.3 12 4zM9.5 5a15 15 0 0 0-1.4 6h-3A8 8 0 0 1 9.5 5zM5.1 13h3a15 15 0 0 0 1.4 6A8 8 0 0 1 5.1 13zM12 20c-.9-1.3-1.7-3.9-1.9-7h3.8c-.2 3.1-1 5.7-1.9 7zm2.5-1a15 15 0 0 0 1.4-6h3a8 8 0 0 1-4.4 6z"/></svg>
      <span>www.fontenotbayou.example</span>
    </li>
  </ul>
  <div class="tagline">First Class <strong>Steak House</strong> with a New Orleans Flare!</div>
</section>

</body>
</html>
```